Waterjet Cutting Business requires an up to date website

We currently have a website which is outdated and in need of modernization.
We are only looking for a simple website with around 4 pages: Home, Contact Us, Materials, Gallery.
We have some pictures and a logo which can be used.
Our primary business is profile cutting of materials to customers specifications using high-pressure water with abrasive.
We are looking for creative ideas and are open to suggestions!
http://brightfordcutworks.com/index.asp?pid=1
Update:
Cut quality picture (uploaded)
Map
Comparison to other profile cutting methods such as plasma/laser
Single page style without continuous scrolling
"We can cut virtually any material from any drawing whether it be a Full 3D cad models to hand sketched "
Target Market(s)
Film Industry, Prototype, Engineering, Architect, Artisits, one off designs
Industry/Entity Type
Engineering
Number of Pages Required
1 page
Font styles to use
Look and feel

```html
<!DOCTYPE html>
<html lang="en">
<head>
<meta charset="UTF-8">
<title>Brightford Cutworks – Materials</title>
<link rel="stylesheet" href="https://fonts.googleapis.com/css2?family=Montserrat:wght@400;500;700;800&family=Lato:wght@400;700&display=swap">
<style>
  :root {
    --ink: #000000;
    --paper: #ffffff;
    --steel-deep: #0b1330;
    --steel-blue: #2a3f8f;
    --magenta: #a0206a;
    --label-text: #111111;
  }
  html, body {
    margin: 0;
    padding: 0;
    width: 1200px;
    height: 675px;
    overflow: hidden;
    background: var(--ink);
  }
  .page {
    position: relative;
    width: 1200px;
    height: 675px;
    overflow: hidden;
    background: var(--ink);
    font-family: "Lato", sans-serif;
    color: var(--paper);
  }
  .backdrop-photo {
    position: absolute;
    inset: 0;
    background:
      radial-gradient(ellipse at 95% 35%, rgba(160,32,106,0.75), transparent 45%),
      radial-gradient(ellipse at 60% 70%, rgba(42,63,143,0.9), transparent 55%),
      linear-gradient(160deg, #1a2556 0%, var(--steel-deep) 60%, #130a22 100%);
  }
  .header-shade {
    position: absolute;
    left: 0; top: 0;
    width: 1200px; height: 114px;
    background: rgba(0,0,0,0.55);
  }
  .dark-sweep {
    position: absolute;
    inset: 0;
  }
  .brand {
    position: absolute;
    left: 178px; top: 40px;
    display: flex;
    align-items: center;
    gap: 10px;
    font-family: "Montserrat", sans-serif;
    font-weight: 800;
    font-size: 22px;
    letter-spacing: 0.5px;
    color: var(--paper);
  }
  .brand-mark {
    width: 14px; height: 14px;
    background: var(--paper);
  }
  .main-nav {
    position: absolute;
    top: 47px;
    left: 597px;
    display: flex;
    align-items: center;
    font-family: "Montserrat", sans-serif;
    font-weight: 500;
    font-size: 14.5px;
    letter-spacing: 0.6px;
  }
  .main-nav a {
    color: var(--paper);
    text-decoration: none;
    margin-right: 27px;
    line-height: 31px;
  }
  .main-nav .nav-contact {
    margin: 0 0 0 17px;
    width: 132px;
    height: 31px;
    background: var(--paper);
    color: var(--label-text);
    border-radius: 5px;
    text-align: center;
  }
  .intro {
    position: absolute;
    left: 178px;
    top: 136px;
    width: 360px;
  }
  .intro-title {
    margin: 0 0 0 -2px;
    font-family: "Montserrat", sans-serif;
    font-weight: 700;
    font-size: 35px;
    letter-spacing: 1.5px;
  }
  .intro-lead {
    margin: 30px 0 0 0;
    font-weight: 700;
    font-size: 14px;
    line-height: 23px;
  }
  .intro-body {
    margin: 18px 0 0 0;
    font-size: 12.3px;
    line-height: 18.4px;
  }
  .material-grid {
    position: absolute;
    left: 605px;
    top: 143px;
    display: grid;
    grid-template-columns: 203px 203px;
    column-gap: 11px;
    row-gap: 31px;
  }
  .material-card {
    width: 203px;
    height: 236px;
    background: var(--paper);
    overflow: hidden;
  }
  .material-card.rounded-right { border-top-right-radius: 14px; }
  .material-card.rounded-left { border-top-left-radius: 14px; }
  .material-photo { height: 193px; }
  .photo-metals { background: linear-gradient(150deg, #0a3a0a, #22b922 55%, #0c2a0c); }
  .photo-stone { background: linear-gradient(160deg, #2a2a2a, #8c8a86 55%, #d7d3cc); }
  .photo-surface { background: linear-gradient(155deg, #3a3f48, #9aa3ad 45%, #24272c); }
  .photo-plastics { background: linear-gradient(150deg, #3a0830, #d22ea6 55%, #5a0c48); }
  .material-label {
    height: 43px;
    line-height: 43px;
    text-align: center;
    font-family: "Montserrat", sans-serif;
    font-size: 14px;
    color: var(--label-text);
  }
</style>
</head>
<body>
<div class="page">
  <div class="backdrop-photo" role="img" aria-label="Close-up of a waterjet cutting head over a metal cutting bed, lit in blue and magenta"></div>
  <div class="header-shade"></div>
  <svg class="dark-sweep" width="1200" height="675" viewBox="0 0 1200 675" aria-hidden="true">
    <path d="M0 0 H655 C648 70 615 140 575 215 C 515 320 500 360 520 430 C 545 520 505 600 528 675 H0 Z" fill="#000000"/>
  </svg>

  <div class="brand"><span class="brand-mark"></span>BRIGHTFORD CUTWORKS</div>

  <nav class="main-nav">
    <a href="#">HOME</a>
    <a href="#">MATERIALS</a>
    <a href="#">GALLERY</a>
    <a href="#" class="nav-contact">CONTACT</a>
  </nav>

  <section class="intro">
    <h1 class="intro-title">Materials</h1>
    <p class="intro-lead">It is possible to cut virtually any profile in any material with waterjet</p>
    <p class="intro-body">Materials we can cut include, but are not limited to, all<br>metals and alloys, stone and ceramics, composites,<br>solid surface, wood, glass, acrylics, resins, silicones, plastics,<br>foams, carpet and felts. We can also cut laminated<br>dissimilar materials which can often be very hard to cut<br>using conventional methods. We are always happy<br>to test cut a sample of your material free of charge to<br>demonstrate the quality of cut achievable.</p>
    <p class="intro-body">Employing Tidecraft's low pressure vacuum assist we can pierce<br>and cut brittle materials such as acrylics,<br>and ceramics. In addition Adaptive Jet technology<br>with Precision Angle Control produces more<br>accurate parts at significantly higher cutting speeds than<br>parts cut with a conventional waterjet.</p>
    <p class="intro-body">If you are not sure whether waterjet cutting will fulfill your<br>requirements give us a call.</p>
  </section>

  <section class="material-grid">
    <article class="material-card">
      <div class="material-photo photo-metals" role="img" aria-label="Waterjet head cutting a metal sheet under green light"></div>
      <div class="material-label">Metals and Alloys</div>
    </article>
    <article class="material-card rounded-right">
      <div class="material-photo photo-stone" role="img" aria-label="Cutting nozzle throwing sparks on a stone slab"></div>
      <div class="material-label">Stone and Cermics</div>
    </article>
    <article class="material-card rounded-left">
      <div class="material-photo photo-surface" role="img" aria-label="Waterjet nozzle cutting a perforated solid surface sheet"></div>
      <div class="material-label">Solid Surface</div>
    </article>
    <article class="material-card rounded-left">
      <div class="material-photo photo-plastics" role="img" aria-label="Cutting bed with plastic parts under magenta light"></div>
      <div class="material-label">Plastics</div>
    </article>
  </section>
</div>
</body>
</html>
```